TranquilPathbyHolt.com

I am looking to advertise our new business offering, tranquilpathbyholt.com, to our local hospice, nursing homes and hospitals. The idea was to have a nice, straightforward colorful postcard with a logo on the front and information on the back. Please peruse the site and utilize any information necessary to convey our concept. Here are the bullet points I'd like on the back of the card:

Tranquil Path by Holt is a cost-effective cremation offering that allows families to arrange for disposition of their loved one in the comfort of their own home.Our promise to you:

1) Your loved one will be transferred into the care of our funeral home with the utmost dignity and respect by the Holt staff. Upon arrival to our facility, they will never leave our care.

2) A trained director will contact the family, via phone, to assist with any questions or concerns.

3) By accessing www.tranquilpathbyholt.com, our intuitive site will take you step-by-step through the cremation arrangement process.

4) A positive identification will be made by the family prior to the cremation process. This will be done securely through our tranquilpathbyholt.com site.

Target Market(s)

Residents of Haywood County needing a low-cost disposition via cremation.

Industry/Entity Type

Business

Font styles to use
Serif

Colors

Designer to choose colors to be used in the design.

Requirements
Must have
• Tasteful design, somewhat of a serene front with a simple logo. The bullet points on the back.
Nice to have
• I have never designed a postcard so I'm relying on a professional to put the must haves.
Should not have
• I'm not looking to place our price on the brochure.

```html
<!DOCTYPE html>
<html lang="en">
<head>
<meta charset="utf-8">
<title>Tranquil Path by Holt – Postcard</title>
<link rel="stylesheet" href="https://fonts.googleapis.com/css2?family=Libre+Baskerville:wght@400;700&family=Open+Sans:ital,wght@1,400;1,700&display=swap">
<style>
  :root{
    --navy:#2c4a7c;
    --navy-dark:#243e69;
    --sky:#cfe0f2;
    --paper:#fbfbf8;
    --cream:#eeebe3;
    --stage:#a9a9a9;
    --ink-line:#3a3a3a;
  }
  *{box-sizing:border-box;margin:0;padding:0}
  html,body{width:1200px;height:979px;overflow:hidden}
  body{background:var(--stage);position:relative;font-family:"Libre Baskerville",serif}

  .card{position:absolute;width:690px;height:455px;box-shadow:0 6px 18px rgba(0,0,0,.25);overflow:hidden}
  .card--front{left:440px;top:24px;background:var(--paper)}
  .card--back{left:70px;top:500px;background:var(--cream)}

  .front-art{position:absolute;inset:0}

  .brand{position:absolute;left:44px;top:58px;color:var(--navy)}
  .brand__name{font-size:31px;font-weight:400;letter-spacing:-.3px;display:block}
  .brand__by{font-size:12px;display:block;margin:4px 0 0 112px}
  .brand__tag{font-size:12px;display:block;margin:6px 0 0 84px}

  .headline{position:absolute;left:36px;top:222px;color:#fff;font-weight:700;line-height:1}
  .headline__top{font-size:27px;letter-spacing:1px;display:block}
  .headline__main{font-size:70px;display:block;margin-top:4px}
  .headline__bottom{font-size:27px;letter-spacing:1px;display:block;margin-top:4px}

  .intro{position:absolute;left:28px;top:24px;width:420px;font-family:"Open Sans",sans-serif;font-style:italic;font-weight:700;font-size:13.5px;line-height:1.28;color:var(--navy)}

  .promises{position:absolute;left:0;top:116px;list-style:none}
  .promise{position:relative;height:44px;margin-bottom:6px;font-family:"Open Sans",sans-serif;font-style:italic;color:#fff}
  .promise svg{position:absolute;left:0;top:0}
  .promise__num{position:absolute;left:24px;top:7px;font-size:24px;font-weight:700}
  .promise__text{position:absolute;left:64px;top:50%;transform:translateY(-50%);font-size:10px;line-height:1.3;white-space:nowrap}

  .site{position:absolute;left:28px;top:330px;font-family:"Open Sans",sans-serif;font-style:italic;font-weight:700;font-size:17px;color:var(--navy);letter-spacing:.4px}

  .stamp{position:absolute;right:44px;top:34px;width:110px;height:72px;border:2px solid var(--ink-line)}
  .address-line{position:absolute;right:44px;width:240px;border-top:1.5px solid var(--ink-line)}
</style>
</head>
<body>

<section class="card card--front" aria-label="Postcard front">
  <svg class="front-art" width="690" height="455" viewBox="0 0 690 455">
    <defs>
      <linearGradient id="skyWash" x1="0" y1="0" x2="0.6" y2="0.6">
        <stop offset="0" stop-color="#b9d2ec"/>
        <stop offset="0.6" stop-color="#fbfbf8"/>
      </linearGradient>
      <radialGradient id="photoTone" cx="0.6" cy="0.5" r="0.7">
        <stop offset="0" stop-color="#6b5644"/>
        <stop offset="0.35" stop-color="#d9c2ad"/>
        <stop offset="1" stop-color="#5c6166"/>
      </radialGradient>
    </defs>
    <rect width="690" height="455" fill="url(#skyWash)"/>
    <polygon fill="url(#photoTone)" points="488,0 690,0 690,455 504,455 304,200" role="img" aria-label="Photo: hands holding a small pot of soil with a green seedling"/>
    <polygon fill="var(--navy)" points="0,185 258,185 450,0 476,0 290,198 494,455 0,455"/>
  </svg>

  <div class="brand">
    <span class="brand__name">Tranquil Path</span>
    <span class="brand__by">by HOLT</span>
    <span class="brand__tag">The Best for Less</span>
  </div>

  <h1 class="headline">
    <span class="headline__top">TRANQUIL</span>
    <span class="headline__main">PATH</span>
    <span class="headline__bottom">WELCOMES YOU</span>
  </h1>
</section>

<section class="card card--back" aria-label="Postcard back">
  <p class="intro">Tranquil Path by Holt is a cost- effective cremation offering that allows families to arrange for disposition of their loved one in the comfort of their own home. Our promise to you:</p>

  <ol class="promises">
    <li class="promise">
      <svg width="440" height="44"><polygon fill="var(--navy)" points="0,0 422,0 440,22 422,44 0,44"/></svg>
      <span class="promise__num">1</span>
      <span class="promise__text">Your loved one will be transferred into the care of our funeral<br>home with the utmost dignity and respect by the Holt staff.<br>Upon arrival to our facility, they will never leave our care.</span>
    </li>
    <li class="promise">
      <svg width="420" height="44"><polygon fill="var(--navy)" points="0,0 402,0 420,22 402,44 0,44"/></svg>
      <span class="promise__num">2</span>
      <span class="promise__text">A trained director will contact the family, via phone, to assist<br>with any questions or concerns.</span>
    </li>
    <li class="promise">
      <svg width="400" height="44"><polygon fill="var(--navy)" points="0,0 382,0 400,22 382,44 0,44"/></svg>
      <span class="promise__num">3</span>
      <span class="promise__text">By accessing www.tranquilpathbyholt.com, our intuitive<br>site will take you step-by-step through the cremation<br>arrangement process.</span>
    </li>
    <li class="promise">
      <svg width="380" height="44"><polygon fill="var(--navy)" points="0,0 362,0 380,22 362,44 0,44"/></svg>
      <span class="promise__num">4</span>
      <span class="promise__text">A positive identification will be made by the family prior<br>to the cremation process. This will be done securely<br>through our tranquilpathbyholt.com site.</span>
    </li>
  </ol>

  <p class="site">www.tranquilpathbyholt.com</p>

  <div class="stamp" aria-label="Stamp area"></div>
  <div class="address-line" style="top:300px"></div>
  <div class="address-line" style="top:340px"></div>
  <div class="address-line" style="top:380px"></div>
</section>

</body>
</html>
```